Investment Management Marketing Presentation

We need a PowerPoint presentation to introduce our new company to prospective investment clients. We are a small, new firm but our founders have 25+ years experience. We pursue an active, very different investment approach that has been very successful. Please see the attached Word doc for additional guidance.

Target Market(s)

Financial institutions, wealthy individuals

Industry/Entity Type

Investment Advisory

Font styles to use
Sans Serif

Colors
3176b5

Requirements
Should not have
• Too many stock photos. Graphic elements are better.

```html
<!DOCTYPE html>
<html lang="en">
<head>
<meta charset="utf-8">
<title>Ridgeline Second Part</title>
<link href="https://fonts.googleapis.com/css2?family=Arimo:wght@400;700&family=Libre+Baskerville:wght@400;700&display=swap" rel="stylesheet">
<style>
:root{
  --ink:#3f3b70;
  --ink-bright:#4a4690;
  --lavender:#e4e3f1;
  --venn-fill:#d6d4ea;
  --grey:#808080;
  --text:#333;
  --rule:#dcdce4;
  --page:#f7f7f7;
  --white:#fff;
}
*{margin:0;padding:0;box-sizing:border-box}
html,body{width:1200px;height:1200px;overflow:hidden;background:var(--page)}
.canvas{position:relative;width:1500px;height:1500px;transform:scale(.8);transform-origin:0 0;font-family:'Arimo',Arial,sans-serif;color:var(--text)}
.slide{position:absolute;width:713px;height:535px;background:var(--white)}
.slide > *{position:absolute}
.title{left:28px;top:28px;font-family:'Libre Baskerville',Georgia,serif;font-size:27px;color:var(--ink);font-weight:400;white-space:nowrap}
.title-rule{left:27px;right:25px;top:73px;height:1px;background:var(--rule)}
.brand{right:28px;top:28px;font-size:13px;color:var(--ink);font-weight:700;letter-spacing:.5px}
.footer-bar{left:0;right:0;top:499px;height:5px;background:var(--ink)}
.footer-mail{left:27px;top:515px;font-size:8px;color:var(--ink)}
.footer-page{right:26px;top:515px;font-size:8px;color:var(--ink)}
.tag{height:34px;color:var(--white);font-weight:700;font-size:15px;display:flex;align-items:center;justify-content:center}
.tag.ink{background:var(--ink)}.tag.bright{background:var(--ink-bright)}.tag.grey{background:var(--grey)}
ul.points{list-style:none;font-size:15px;line-height:29px}
ul.points li{padding-left:14px;position:relative}
ul.points li::before{content:"•";position:absolute;left:0;font-size:12px}
ul.tight{line-height:17px;font-size:14px}
ul.tight li{margin-bottom:10px}
.vrule{width:1px;background:var(--rule)}
.band{left:0;right:0;background:var(--ink);color:var(--white)}
.band-serif{font-family:'Libre Baskerville',Georgia,serif;font-size:17px;display:flex;align-items:center;justify-content:center}
.quote-mark{left:82px;top:402px;width:64px;height:64px;border-radius:50%;background:var(--white);color:var(--ink);font-family:'Libre Baskerville',Georgia,serif;font-weight:700;font-size:64px;line-height:92px;text-align:center}
.quote-text{left:170px;top:400px;font-size:17px;line-height:22px}
.quote-by{font-size:11px;margin-top:8px;display:block}
.icon{width:78px;height:78px}
.perf{left:27px;top:137px;width:662px;border-collapse:collapse;font-size:10px;text-align:center}
.perf th{background:var(--ink);color:var(--white);height:54px;font-size:11px;font-weight:700;line-height:14px;border-right:1px solid #5a5690}
.perf td{height:50px;border-bottom:1px solid var(--rule);border-right:1px solid var(--rule);line-height:12px;color:#444}
.perf td:first-child{text-align:left;padding-left:7px}
.perf tr.shade td{background:var(--lavender);font-weight:700;color:var(--ink);font-size:12px}
.perf .hl{border-left:2px solid var(--ink-bright);border-right:2px solid var(--ink-bright)}
.perf tr:last-child .hl{border-bottom:2px solid var(--ink-bright)}
.perf th.hl{border-top:2px solid var(--ink-bright)}
.fineprint{left:27px;top:463px;width:662px;font-size:8px;line-height:10px;color:#777}
.caption{position:absolute;left:24px;top:1243px;font-size:74px;font-weight:700;color:#111;white-space:nowrap}
</style>
</head>
<body>
<div class="canvas">

  <section class="slide" style="left:23px;top:42px">
    <h1 class="title">Boldly Different</h1>
    <div class="brand">Ridgeline</div>
    <div class="title-rule"></div>
    <div class="tag ink" style="left:27px;top:117px;width:320px">Departing from Benchmarks</div>
    <div class="tag grey" style="left:366px;top:117px;width:320px">Delivers Superior Performance</div>
    <ul class="points" style="left:30px;top:165px">
      <li>Concentrated and Selective</li><li>High Conviction</li><li>Moderate Turnover</li><li>High Active Share</li>
    </ul>
    <div class="vrule" style="left:357px;top:160px;height:200px"></div>
    <ul class="points" style="left:374px;top:167px">
      <li>High Alpha</li><li>Higher Sharpe Ratio</li><li>Lower Beta</li><li>Asymmetric Risk Profile</li><li>Low Correlation</li>
    </ul>
    <div class="band" style="top:378px;height:117px"></div>
    <div class="quote-mark">“</div>
    <p class="quote-text" style="color:var(--white)">If you want to have a <b>better performance than the crowd</b>,<br>you must <b>do things differently</b> from the crowd<span class="quote-by">- Sir Edmund Hale</span></p>
    <div class="footer-bar"></div>
    <div class="footer-mail">ClientDesk@ArborlineFS.com</div>
    <div class="footer-page">5</div>
  </section>

  <section class="slide" style="left:763px;top:42px">
    <h1 class="title">Ridgeline Leverages Two Alpha Drivers</h1>
    <div class="brand">Ridgeline</div>
    <div class="title-rule"></div>
    <svg style="left:0;top:100px" width="713" height="340" viewBox="0 100 713 340">
      <defs><clipPath id="left-circle"><circle cx="265" cy="281" r="125"/></clipPath></defs>
      <circle cx="448" cy="281" r="125" fill="var(--venn-fill)" clip-path="url(#left-circle)"/>
      <circle cx="265" cy="281" r="125" fill="none" stroke="var(--ink)" stroke-width="6"/>
      <circle cx="448" cy="281" r="125" fill="none" stroke="var(--grey)" stroke-width="6"/>
      <g font-family="Arimo, Arial, sans-serif" font-size="15" fill="#333" text-anchor="middle">
        <text x="265" y="132">Fundamental</text><text x="448" y="132">Behavioral</text>
      </g>
      <g font-family="Libre Baskerville, Georgia, serif" font-size="15" font-weight="700" text-anchor="middle">
        <text x="232" y="283" fill="var(--ink)">ACCELERATING</text><text x="235" y="302" fill="var(--ink)">GROWTH</text>
        <text x="476" y="283" fill="#444">PRICE</text><text x="478" y="302" fill="#444">MOMENTUM</text>
      </g>
    </svg>
    <div class="band band-serif" style="top:445px;height:50px;font-size:18px">VALUATION AND RISK</div>
    <div class="footer-bar"></div>
    <div class="footer-mail">ClientDesk@ArborlineFS.com</div>
    <div class="footer-page">6</div>
  </section>

  <section class="slide" style="left:20px;top:601px;width:716px">
    <h1 class="title">Monitor, Modify and Sell Discipline</h1>
    <div class="brand">Ridgeline</div>
    <div class="title-rule"></div>
    <p style="left:27px;top:83px;font-size:13px"><b>Objective:</b> Cut losses quickly and let the winners run</p>
    <svg class="icon" style="left:93px;top:127px" viewBox="0 0 78 78">
      <circle cx="39" cy="39" r="37" fill="none" stroke="var(--ink)" stroke-width="2.5"/>
      <rect x="27" y="22" width="26" height="30" rx="2" fill="var(--ink)"/>
      <g stroke="var(--white)" stroke-width="2"><line x1="32" y1="30" x2="48" y2="30"/><line x1="32" y1="36" x2="48" y2="36"/><line x1="32" y1="42" x2="48" y2="42"/></g>
      <rect x="23" y="50" width="24" height="6" rx="3" fill="var(--ink)"/>
    </svg>
    <svg class="icon" style="left:314px;top:127px" viewBox="0 0 78 78">
      <circle cx="39" cy="39" r="37" fill="none" stroke="var(--ink)" stroke-width="2.5"/>
      <text x="36" y="32" font-family="Arimo, Arial, sans-serif" font-weight="700" font-size="20" fill="var(--ink)" text-anchor="middle">$</text>
      <g fill="none" stroke="var(--ink)" stroke-width="2.5"><ellipse cx="36" cy="40" rx="12" ry="4"/><path d="M24 40v14c0 2 5 4 12 4s12-2 12-4V40"/><path d="M24 47c0 2 5 4 12 4s12-2 12-4"/><path d="M50 38l8-8m-6 0h6v6"/></g>
    </svg>
    <svg class="icon" style="left:545px;top:127px" viewBox="0 0 78 78">
      <circle cx="39" cy="39" r="37" fill="none" stroke="var(--grey)" stroke-width="2.5"/>
      <path d="M39 24a11 11 0 0 0-7 19c2 2 3 4 3 6h8c0-2 1-4 3-6a11 11 0 0 0-7-19z" fill="var(--grey)"/>
      <rect x="35" y="51" width="8" height="5" rx="1" fill="var(--grey)"/>
      <g stroke="var(--grey)" stroke-width="2"><line x1="39" y1="14" x2="39" y2="19"/><line x1="24" y1="21" x2="27" y2="25"/><line x1="54" y1="21" x2="51" y2="25"/><line x1="18" y1="35" x2="23" y2="35"/><line x1="60" y1="35" x2="55" y2="35"/></g>
    </svg>
    <div class="tag ink" style="left:27px;top:217px;width:208px">Monitor</div>
    <div class="tag bright" style="left:253px;top:217px;width:208px">Sales Triggers</div>
    <div class="tag grey" style="left:480px;top:217px;width:208px">Hold or trade?</div>
    <ul class="points tight" style="left:30px;top:266px;width:200px">
      <li>Alpha factors</li><li>Investment policy compliance</li><li>Return contributors</li><li>Unintended or excessive risks</li>
    </ul>
    <div class="vrule" style="left:245px;top:255px;height:170px"></div>
    <ul class="points tight" style="left:260px;top:266px;width:200px">
      <li>Decelerating growth or negative surprise</li><li>Diminished outlook or increasing risk</li><li>Deteriorating relative strength</li>
    </ul>
    <div class="vrule" style="left:471px;top:255px;height:170px"></div>
    <ul class="points tight" style="left:490px;top:266px;width:200px">
      <li>Occasionally add on weakness or strength</li><li>Rarely trim</li>
    </ul>
    <div class="band band-serif" style="top:445px;height:50px">Ridgeline Edge:&nbsp; Maximize upside, manage risk, and keep turnover low</div>
    <div class="footer-bar"></div>
    <div class="footer-mail">ClientDesk@ArborlineFS.com</div>
    <div class="footer-page">7</div>
  </section>

  <section class="slide" style="left:763px;top:601px">
    <h1 class="title">Superior Performance Since 1999</h1>
    <div class="brand">Ridgeline</div>
    <div class="title-rule"></div>
    <p style="left:27px;top:83px;width:665px;font-size:13px;line-height:17px">Whether applied by a team running a billion dollar portfolio or a solo manager incubating multiple strategies, this discipline has consistently delivered strong and uncorrelated risk-adjusted returns.</p>
    <table class="perf">
      <tr><th style="width:156px"></th><th>Meridian<br>(1999 - 2009)</th><th>Small Cap Growth<br>(1/11 - 4/14)</th><th>SMid Growth<br>(10/11 - 4/14)</th><th class="hl">Small Cap Growth<br>(1/16 - 1/19)</th></tr>
      <tr><td>Excess Return<br>Annualized Returns</td><td>5.06%<br>8.41% v. 3.35%</td><td>0.88%<br>14.25% v. 13.37%</td><td>3.70%<br>21.24% v. 17.55%</td><td class="hl">0.21%<br>11.12% v. 10.90%</td></tr>
      <tr class="shade"><td>Alpha</td><td>5.68%</td><td>3.39%</td><td>5.77%</td><td class="hl">5.63%</td></tr>
      <tr class="shade"><td>Beta</td><td>0.88</td><td>0.84</td><td>0.85</td><td class="hl">0.47</td></tr>
      <tr><td>Volatility</td><td>25.4% v. 24.3%</td><td>18.7% v. 17.1%</td><td>11.1% v. 10.6%</td><td class="hl">11.8% v. 17.3%</td></tr>
      <tr><td>R² to Total Market 3000</td><td>0.45</td><td>0.55 v. 0.87</td><td>0.56 v. 0.85</td><td class="hl">0.48 v. 0.82</td></tr>
    </table>
    <p class="fineprint">This table is presented as supplemental information. Statistics are calculated from monthly returns before management fees. Earlier returns were adjusted to remove the estimated impact of excess cash and are only approximate fully invested portfolio returns. Returns have not been audited. Benchmarks reflect broad growth indexes for each period shown.</p>
    <div class="footer-bar" style="height:2px;top:503px"></div>
    <div class="footer-mail">ClientDesk@ArborlineFS.com</div>
    <div class="footer-page">8</div>
  </section>

  <div class="caption">Ridgeline Second Part</div>
</div>
</body>
</html>
```